Direct to Consumer extended service contract business with a new disruptive business model needs a

We need a customized wordpress design for a company called 'Tall Harbor Assurance'.
We provide an innovative and unique service contract protection program direct to consumers. This program provides monthly coverage for all electronics purchased in the last 4 years and all electronics the consumer purchases in the future for a low monthly fee. The overall design should communicate a sense of legitimacy, ethics, and superior customer service and support (in an industry that has a huge PR issue to overcome).
Electronics is the first product group, other product groups with different price points to launch in the future..

Target Market(s)

All purchasers of electronic goods...all demographics

Industry/Entity Type

Electronics

Font styles to use
Sans Serif

Requirements
Must have
• Customer Testimonials
Industry News
Customer ratings
Blog posts
Call to action messaging
Like the functional elements and design of bramblequill.example (need to be better)
Nice to have
• Like to see video testimonials
Social network "whats trending related to electronics or service contract industry"
Easy way to register products for warranty

```html
<!DOCTYPE html>
<html lang="en">
<head>
<meta charset="utf-8">
<title>Tall Harbor Assurance</title>
<link href="https://fonts.googleapis.com/css2?family=Lato:wght@300;400;700;900&display=swap" rel="stylesheet">
<style>
:root{
  --blue:#1e7bc4;
  --blue-dark:#15609e;
  --blue-deep:#0f4f86;
  --ink:#333a40;
  --muted:#7b848c;
  --line:#e3e7ea;
  --orange:#f5a31a;
  --topbar:#2b3035;
  --footer:#eef1f3;
  --white:#ffffff;
}
*{box-sizing:border-box;margin:0;padding:0}
html,body{width:872px;height:1200px;overflow:hidden;background:var(--white)}
body{font-family:"Lato",Arial,sans-serif;color:var(--ink);position:relative}
.topbar{height:22px;background:var(--topbar);display:flex;justify-content:space-between;align-items:center;padding:0 70px;font-size:9px;color:#c4cacf}
.topbar .social{display:flex;gap:6px}
.topbar .social span{width:10px;height:10px;border-radius:50%;background:#5b636a;display:block}
.topbar .contact{display:flex;gap:14px}
.header{height:78px;display:flex;align-items:center;justify-content:space-between;padding:0 70px;border-bottom:1px solid var(--line)}
.brand{font-size:18px;font-weight:700;color:var(--blue);letter-spacing:.5px;display:flex;align-items:center;gap:8px;white-space:nowrap}
.brand .mark{width:14px;height:14px;background:var(--blue);display:block;flex:none}
.nav{display:flex;gap:18px;font-size:12px;color:var(--ink);white-space:nowrap}
.nav a{color:inherit;text-decoration:none}
.hero{height:370px;background:linear-gradient(160deg,var(--blue) 0%,var(--blue-dark) 70%,var(--blue-deep) 100%);position:relative;color:var(--white)}
.hero-devices{position:absolute;left:150px;top:22px;width:220px;height:250px;border-radius:10px;background:linear-gradient(120deg,#3a4048,#1b1f24 60%,#4d5660)}
.hero-copy{position:absolute;left:440px;top:40px;width:360px}
.hero-copy .kicker{font-size:17px;font-weight:300;letter-spacing:1px}
.hero-copy h1{font-size:31px;font-weight:900;letter-spacing:.5px;margin-top:2px}
.quote{display:flex;gap:12px;margin-top:22px;align-items:flex-start}
.avatar{flex:none;width:54px}
.avatar .photo{width:54px;height:54px;border-radius:4px;background:linear-gradient(#c9b29a,#8a715c)}
.avatar p{font-size:9px;text-align:center;margin-top:4px}
.bubble{background:var(--white);color:var(--ink);border-radius:6px;padding:12px 14px;font-size:11px;line-height:1.45;font-style:italic;position:relative}
.bubble::before{content:"";position:absolute;left:-8px;top:16px;border:8px solid transparent;border-left:0;border-right-color:var(--white)}
.register{position:absolute;left:0;right:0;top:282px;height:88px;background:rgba(10,50,90,.35);text-align:center;padding-top:12px}
.register h2{font-size:20px;font-weight:400}
.signup{display:flex;justify-content:center;gap:10px;margin-top:12px}
.field{height:28px;background:var(--white);border-radius:3px;color:var(--muted);font-size:11px;display:flex;align-items:center;justify-content:space-between;padding:0 10px}
.field.select{width:160px}
.field.input{width:230px}
.btn{height:28px;width:160px;background:var(--orange);color:var(--white);font-weight:700;font-size:12px;border-radius:3px;display:flex;align-items:center;justify-content:center;letter-spacing:.5px}
.section-title{text-align:center;font-size:19px;font-weight:700;color:var(--ink)}
.why{height:150px;padding-top:20px;background:#f7f9fa}
.features{display:flex;gap:30px;padding:0 90px;margin-top:22px}
.feature{flex:1;display:flex;gap:10px}
.feature .icon{flex:none;width:30px;height:30px;background:var(--blue);border-radius:3px;display:flex;align-items:center;justify-content:center}
.feature h3{font-size:12px;color:var(--blue);font-weight:700}
.feature p{font-size:10px;color:var(--muted);line-height:1.45;margin-top:4px}
.clients{height:230px;padding-top:18px}
.videos{display:flex;gap:20px;padding:0 70px;margin-top:16px}
.video{flex:1}
.video .thumb{height:112px;border-radius:2px;background:linear-gradient(135deg,#b9c2ca,#6f7a84);position:relative;display:flex;align-items:center;justify-content:center}
.video .thumb::after{content:"";position:absolute;left:0;right:0;bottom:0;height:12px;background:rgba(0,0,0,.55)}
.video h4{font-size:12px;margin-top:8px}
.video p{font-size:10px;color:var(--muted);font-style:italic;line-height:1.4;margin-top:3px}
.columns{height:206px;display:flex;gap:26px;padding:14px 70px 0;border-top:1px solid var(--line)}
.col{flex:1}
.col h3{font-size:15px;color:var(--blue);font-weight:700;margin-bottom:10px}
.item{display:flex;gap:10px;margin-bottom:12px}
.item .pic{flex:none;width:42px;height:38px;background:linear-gradient(135deg,#a9b4bd,#5e6a74);border-radius:2px}
.item p{font-size:10px;color:var(--ink);line-height:1.4}
.item time{display:block;font-size:9px;color:var(--muted);margin-top:2px}
.rating{border-bottom:1px solid var(--line);padding-bottom:9px;margin-bottom:10px}
.rating .row{display:flex;justify-content:space-between;font-size:10px;font-style:italic}
.rating .stars{color:var(--orange);font-style:normal;letter-spacing:1px}
.rating a{font-size:9px;color:var(--blue);display:block;margin-top:3px;text-decoration:none}
.footer{height:112px;background:var(--footer);display:flex;padding:14px 70px 0;gap:30px}
.footer .brand-block{width:150px}
.footer .brand{font-size:16px;line-height:1.1;white-space:normal}
.badges{display:flex;gap:8px;margin-top:10px}
.badges span{width:48px;height:22px;background:var(--blue-deep);border-radius:2px;display:block}
.badges span + span{width:26px;background:#4a5258}
.fcol h4{font-size:11px;margin-bottom:6px}
.fcol ul{list-style:none;font-size:9px;color:var(--muted);line-height:1.55}
.fcol.contact li{display:flex;gap:5px;align-items:center;white-space:nowrap}
.cards{display:flex;gap:5px}
.cards span{width:28px;height:18px;border-radius:2px;background:#c9d1d7;display:block}
.bottombar{height:32px;background:var(--topbar);color:#c4cacf;font-size:9px;display:flex;justify-content:space-between;align-items:center;padding:0 70px}
</style>
</head>
<body>
<div class="topbar">
  <div class="social"><span></span><span></span><span></span><span></span></div>
  <div class="contact"><span>1-800-555-0142</span><span>help@tallharbor.example</span></div>
</div>

<header class="header">
  <div class="brand"><span class="mark"></span>TALL HARBOR ASSURANCE</div>
  <nav class="nav">
    <a href="#">Phones</a><a href="#">Slates</a><a href="#">Laptops</a><a href="#">Tablets/eReaders</a><a href="#">Smartphones</a><a href="#">Cameras</a><a href="#">Televisions</a>
  </nav>
</header>

<section class="hero">
  <div class="hero-devices" role="img" aria-label="Two smartphones shown front and back"></div>
  <div class="hero-copy">
    <div class="kicker">PROTECT YOUR PHONE</div>
    <h1>HERE TO HELP, 24/7</h1>
    <div class="quote">
      <div class="avatar">
        <div class="photo" role="img" aria-label="Customer portrait"></div>
        <p>Lena Ford</p>
      </div>
      <div class="bubble">"Thanks to TALL HARBOR ASSURANCE, I have my phone back right away. Very good service. 100% Recommended to all!"</div>
    </div>
  </div>
  <div class="register">
    <h2>Register today and start protecting you phone.</h2>
    <div class="signup">
      <div class="field select">Phone <svg width="8" height="5"><path d="M0 0h8L4 5z" fill="#7b848c"/></svg></div>
      <div class="field input">Email</div>
      <div class="btn">SIGN UP NOW</div>
    </div>
  </div>
</section>

<section class="why">
  <h2 class="section-title">Why Choose Tall Harbor Assurance?</h2>
  <div class="features">
    <div class="feature">
      <div class="icon"><svg width="16" height="14"><path d="M1 1h14v9H6l-4 3v-3H1z" fill="#fff"/></svg></div>
      <div><h3>Here To Help, 24/7</h3><p>Real people answer every call, any hour of any day, all year.</p></div>
    </div>
    <div class="feature">
      <div class="icon"><svg width="16" height="16"><path d="M8 2a6 6 0 1 0 6 6" stroke="#fff" stroke-width="2" fill="none"/><path d="M11 1l4 2-3 3z" fill="#fff"/></svg></div>
      <div><h3>Fixed or Replaced Fast</h3><p>Most devices are repaired or swapped within days, not weeks.</p></div>
    </div>
    <div class="feature">
      <div class="icon"><svg width="16" height="14"><path d="M2 7l4 4 8-9" stroke="#fff" stroke-width="2.5" fill="none"/></svg></div>
      <div><h3>You're Covered</h3><p>One low monthly fee protects every device you own today.</p></div>
    </div>
  </div>
</section>

<section class="clients">
  <h2 class="section-title">What Our Clients Say?</h2>
  <div class="videos">
    <div class="video">
      <div class="thumb" role="img" aria-label="Video testimonial still of a customer"><svg width="30" height="30"><circle cx="15" cy="15" r="14" fill="rgba(255,255,255,.85)"/><path d="M12 9l9 6-9 6z" fill="#1e7bc4"/></svg></div>
      <h4>Mara Loft</h4>
      <p>"My cracked screen was replaced in two days. Friendly team, no hassle."</p>
    </div>
    <div class="video">
      <div class="thumb" role="img" aria-label="Video testimonial still of a customer on the phone"><svg width="30" height="30"><circle cx="15" cy="15" r="14" fill="rgba(255,255,255,.85)"/><path d="M12 9l9 6-9 6z" fill="#1e7bc4"/></svg></div>
      <h4>Owen Reddick</h4>
      <p>"Filing a claim took five minutes online. Honest people, clear terms."</p>
    </div>
    <div class="video">
      <div class="thumb" role="img" aria-label="Video testimonial still of a customer"><svg width="30" height="30"><circle cx="15" cy="15" r="14" fill="rgba(255,255,255,.85)"/><path d="M12 9l9 6-9 6z" fill="#1e7bc4"/></svg></div>
      <h4>Petra Vale</h4>
      <p>"Every gadget in our home is covered now. Worth every single penny."</p>
    </div>
  </div>
</section>

<section class="columns">
  <div class="col">
    <h3>Industry News</h3>
    <div class="item"><div class="pic" role="img" aria-label="News photo"></div><p>New rules bring clearer terms to service contracts nationwide.<time>October 12, 2013</time></p></div>
    <div class="item"><div class="pic" role="img" aria-label="News photo"></div><p>Repair costs for smartphones rise again this season.<time>October 10, 2013</time></p></div>
    <div class="item"><div class="pic" role="img" aria-label="News photo"></div><p>Consumers keep their electronics longer than ever before.<time>October 08, 2013</time></p></div>
  </div>
  <div class="col">
    <h3>Latest Blog</h3>
    <div class="item"><div class="pic" role="img" aria-label="Blog photo"></div><p>Five simple ways to keep your laptop running smoothly.<time>October 11, 2013</time></p></div>
    <div class="item"><div class="pic" role="img" aria-label="Blog photo"></div><p>How to register your devices in under two minutes.<time>October 09, 2013</time></p></div>
    <div class="item"><div class="pic" role="img" aria-label="Blog photo"></div><p>What a good protection plan should always include.<time>October 07, 2013</time></p></div>
  </div>
  <div class="col">
    <h3>User Ratings</h3>
    <div class="rating"><div class="row"><span>"Quick claim and kind support staff."</span><span class="stars">★★★★★</span></div><a href="#">Read review</a></div>
    <div class="rating"><div class="row"><span>"Clear pricing, no surprises at all."</span><span class="stars">★★★★★</span></div><a href="#">Read review</a></div>
    <div class="rating"><div class="row"><span>"Tablet replaced within the same week."</span><span class="stars">★★★★★</span></div><a href="#">Read review</a></div>
  </div>
</section>

<footer class="footer">
  <div class="brand-block">
    <div class="brand">TALL HARBOR<br>ASSURANCE</div>
    <div class="badges"><span></span><span></span></div>
  </div>
  <div class="fcol">
    <h4>Navigation</h4>
    <ul><li>Home</li><li>Services</li><li>About</li><li>Blog</li></ul>
  </div>
  <div class="fcol">
    <h4>Services</h4>
    <ul><li>Phones</li><li>Laptops</li><li>Tablets</li><li>Cameras</li></ul>
  </div>
  <div class="fcol contact">
    <h4>Contact us</h4>
    <ul>
      <li><svg width="8" height="8"><path d="M2 0l2 2-1 1 2 2 1-1 2 2-2 2C3 8 0 5 0 2z" fill="#7b848c"/></svg>1-800-555-0142</li>
      <li><svg width="8" height="8"><rect x="0" y="1" width="8" height="6" fill="none" stroke="#7b848c"/><path d="M0 1l4 3 4-3" stroke="#7b848c" fill="none"/></svg>help@tallharbor.example</li>
      <li><svg width="8" height="9"><path d="M4 0a3 3 0 0 1 3 3c0 2-3 6-3 6S1 5 1 3a3 3 0 0 1 3-3z" fill="#7b848c"/></svg>210 Harbor Lane, Suite 4</li>
      <li>Portside, NY 10001</li>
    </ul>
  </div>
  <div class="fcol">
    <h4>We Accept</h4>
    <div class="cards"><span></span><span></span><span></span></div>
  </div>
</footer>

<div class="bottombar">
  <span>Copyright 2013 All Rights Reserved</span>
  <span>Site Map &nbsp;•&nbsp; Privacy Policy</span>
</div>
</body>
</html>
```